Security based company delivering High Risk Training to Law Enforcement Agencies Worldwide.

We need a Web design for a company doing business in Washington D.C. We deliver High Risk Training to Law Enforcement Agencies throughout the world. Our focus is on Improvised Explosive Devices. We train Bomb Technicians and First Responders in all aspects relating to bombings and criminal incidents globally.

Reason: We have uploaded our logo. Thank you.

Target Market(s)

Military and Law Enforcement Personnel from around the world.

Industry/Entity Type

Business

Requirements
Should not have
• Do not include cartoon like characters.

```html
<!DOCTYPE html>
<html lang="en">
<head>
<meta charset="utf-8">
<title>High Risk Training</title>
<link rel="stylesheet" href="https://fonts.googleapis.com/css2?family=Cabin:wght@400;600;700&family=PT+Sans:wght@400;700&display=swap">
<style>
:root{
  --orange:#e8671c;
  --ink:#0d0d0d;
  --nav:#2a2a2a;
  --nav-line:#151515;
  --khaki:#c9c08a;
  --olive:#8a8a5a;
  --light:#e6e6e6;
  --muted:#9a9a9a;
  --footer:#262626;
  --body-dark:#555;
  --white:#ffffff;
}
*{margin:0;padding:0;box-sizing:border-box}
html,body{width:675px;height:1200px;overflow:hidden;background:var(--white)}
body{font-family:"Cabin",sans-serif;position:relative}
.page{position:relative;width:675px;height:1200px;overflow:hidden}

/* header */
.site-header{position:absolute;left:0;top:0;width:675px;height:115px;background:linear-gradient(#111,#060606)}
.brand{position:absolute;left:48px;top:40px;font-family:"PT Sans",sans-serif;font-size:42px;color:var(--orange);line-height:1}
.header-phone{position:absolute;right:50px;top:37px;font-family:"PT Sans",sans-serif;font-size:15px;color:var(--white);display:flex;align-items:center;gap:7px}
.search{position:absolute;left:487px;top:70px;width:138px;height:20px;border-radius:3px;background:#2c2c2c;border:1px solid #3a3a3a;font-size:8px;color:#888;padding:5px 6px;line-height:1}
.search svg{position:absolute;right:5px;top:4px}

/* navigation */
.main-nav{position:absolute;left:0;top:115px;width:675px;height:33px;background:linear-gradient(#3a3a3a,#222);border-top:1px solid #444}
.main-nav ul{list-style:none;position:absolute;left:48px;top:0;display:flex;height:33px}
.main-nav li{height:33px;line-height:33px;font-size:10.5px;font-weight:700;color:var(--white);text-align:center;border-right:1px solid var(--nav-line);box-shadow:1px 0 0 #444}
.main-nav li.active{background:var(--orange);border-right:none;box-shadow:none}

/* hero */
.hero{position:absolute;left:0;top:148px;width:675px;height:282px;background:linear-gradient(90deg,#6b6a50 0%,#b9b2a2 30%,#c9c3b6 60%,#ddd6c8 100%)}
.hero-arrow{position:absolute;top:120px}
.hero-arrow.prev{left:47px}
.hero-arrow.next{left:590px}

/* services */
.services{position:absolute;left:0;top:430px;width:675px;height:308px;background:radial-gradient(ellipse at 50% 20%,#2a2a2a,#0b0b0b 70%)}
.services h2{position:absolute;top:36px;width:100%;text-align:center;font-weight:400;font-size:19px;color:var(--khaki)}
.services .intro{position:absolute;left:50px;top:70px;width:575px;text-align:center;font-size:8.5px;line-height:15px;color:var(--light)}
.service{position:absolute;top:124px;width:170px;text-align:center}
.service .badge{display:block;margin:0 auto}
.service h3{margin-top:10px;font-weight:400;font-size:13px;color:var(--khaki)}
.service h3.dim{color:var(--olive)}
.service p{margin-top:6px;font-size:8.5px;line-height:15px;color:var(--light)}

/* welcome */
.welcome{position:absolute;left:0;top:738px;width:675px;height:249px;background:var(--white)}
.soldier-photo{position:absolute;left:48px;top:32px;width:144px;height:217px;background:linear-gradient(#8c7c62,#6e5f49 60%,#5a4e3d);border-radius:40px 40px 0 0}
.welcome-text{position:absolute;left:220px;top:40px;width:200px}
.welcome-text h2,.news h2{font-weight:400;font-size:18.5px;color:#222;letter-spacing:-.2px}
.welcome-text p{margin-top:10px;font-size:8.3px;line-height:15px;color:var(--body-dark)}
.welcome-text p + p{margin-top:3px}
.read-more{display:inline-block;margin-top:14px;border:1px solid #444;padding:0 9px;height:24px;line-height:23px;font-size:9px;color:#222}
.news{position:absolute;left:470px;top:40px;width:157px}
.news-item{border-bottom:1px solid #ddd;padding:15px 0 10px}
.news-item:last-child{border-bottom:none}
.news-item h3{font-size:8.5px;font-weight:700;color:#7a7a45;white-space:nowrap}
.news-item p{margin-top:10px;font-size:8.3px;line-height:15px;color:var(--body-dark)}

/* footer */
.site-footer{position:absolute;left:0;top:987px;width:675px;height:213px;background:var(--footer)}
.site-footer h2{font-weight:400;font-size:13px;color:var(--white)}
.col{position:absolute;top:30px}
.col.testimonials{left:48px;width:200px}
.col.contact{left:302px;width:150px}
.col.follow{left:470px;width:160px;top:32px}
.quote{position:relative;margin-top:12px;padding-left:10px;font-style:italic;font-size:7.8px;line-height:14px;color:var(--light)}
.quote::before{content:"\201C";position:absolute;left:0;top:-4px;font-size:14px;color:#888;font-style:normal}
.quote::after{content:"\201D";position:absolute;right:-4px;bottom:-12px;font-size:14px;color:#888;font-style:normal}
.author{margin-top:7px;text-align:right;font-size:8px;font-weight:700;color:var(--white);display:flex;justify-content:flex-end;align-items:center;gap:5px}
.contact-list{list-style:none;margin-top:12px}
.contact-list li{display:flex;gap:9px;font-size:8.3px;line-height:15px;color:var(--light);margin-bottom:5px}
.contact-list svg{flex:none;margin-top:3px}
.follow p{margin-top:10px;font-size:8.3px;line-height:15px;color:var(--light)}
.social{display:flex;gap:8px;margin-top:10px}
.social span{width:27px;height:27px;border:1.5px solid #cfcfcf;border-radius:50%}
.footer-rule{position:absolute;left:48px;top:165px;width:579px;height:1px;background:#3a3a3a}
.copyright{position:absolute;left:48px;top:186px;font-size:8.3px;color:var(--light)}
</style>
</head>
<body>
<div class="page">

  <header class="site-header">
    <div class="brand">Logo</div>
    <div class="header-phone">+1 202 555 0147
      <svg width="12" height="13" viewBox="0 0 24 24"><path fill="#fff" d="M6.6 10.8a15.1 15.1 0 0 0 6.6 6.6l2.2-2.2a1 1 0 0 1 1-.25 11.4 11.4 0 0 0 3.6.57 1 1 0 0 1 1 1V20a1 1 0 0 1-1 1A17 17 0 0 1 3 4a1 1 0 0 1 1-1h3.5a1 1 0 0 1 1 1c0 1.25.2 2.45.57 3.57a1 1 0 0 1-.25 1z"/></svg>
    </div>
    <div class="search">Search..
      <svg width="10" height="10" viewBox="0 0 12 12"><circle cx="5" cy="5" r="3.5" fill="none" stroke="#777" stroke-width="1.4"/><line x1="7.6" y1="7.6" x2="11" y2="11" stroke="#777" stroke-width="1.6"/></svg>
    </div>
  </header>

  <nav class="main-nav">
    <ul>
      <li class="active" style="width:62px">HOME</li>
      <li style="width:86px">ABOUT US</li>
      <li style="width:83px">SERVICES</li>
      <li style="width:86px">TRAININGS</li>
      <li style="width:103px">TESTIMONIALS</li>
      <li style="width:66px">BLOG</li>
      <li style="width:93px;border-right:none;box-shadow:none">CONTACT US</li>
    </ul>
  </nav>

  <section class="hero" role="img" aria-label="Bomb technician in a protective suit kneeling beside a device near a stop sign and concrete wall">
    <svg class="hero-arrow prev" width="36" height="36" viewBox="0 0 36 36"><circle cx="18" cy="18" r="18" fill="rgba(40,40,40,.6)"/><path d="M20.5 12l-6 6 6 6" fill="none" stroke="#fff" stroke-width="1.6"/></svg>
    <svg class="hero-arrow next" width="36" height="36" viewBox="0 0 36 36"><circle cx="18" cy="18" r="18" fill="rgba(40,40,40,.6)"/><path d="M15.5 12l6 6-6 6" fill="none" stroke="#fff" stroke-width="1.6"/></svg>
  </section>

  <section class="services">
    <h2>Our Services</h2>
    <p class="intro">Typi non habent claritatem insitam; est usus legentis in iis qui facit eorum claritatem. Investigationes demonstraverunt lectores legere me lquod ii unt saepius. Clarit as est etiam processus dynamicus, qui sequitur mutationem consuetudium lectorum. Mirum est notare quam litteothic.</p>

    <div class="service" style="left:37px">
      <svg class="badge" width="70" height="70" viewBox="0 0 70 70"><circle cx="35" cy="35" r="33" fill="#111" stroke="#3a3a3a" stroke-width="3"/>
        <g fill="none" stroke="#e8e2b8" stroke-width="2"><circle cx="35" cy="35" r="5"/><path d="M35 23v4M35 43v4M23 35h4M43 35h4M26.5 26.5l2.8 2.8M40.7 40.7l2.8 2.8M26.5 43.5l2.8-2.8M40.7 29.3l2.8-2.8"/><circle cx="35" cy="35" r="10"/></g></svg>
      <h3>High Risk Training</h3>
      <p>Claritas est eteus dynamicuinquiqu conetlaritasdynamicusClaritas est nihil imp fiant sollemnes feiat lla.</p>
    </div>

    <div class="service" style="left:250px">
      <svg class="badge" width="70" height="70" viewBox="0 0 70 70"><circle cx="35" cy="35" r="33" fill="#111" stroke="#3a3a3a" stroke-width="3"/>
        <g fill="#e8e2b8"><rect x="28" y="28" width="12" height="5" rx="1"/><rect x="40" y="29.5" width="12" height="2"/><rect x="20" y="33" width="30" height="5" rx="1"/><rect x="18" y="38" width="34" height="6" rx="3"/></g></svg>
      <h3 class="dim">Explosive Devices</h3>
      <p>Claritas est eteus dynamicuinquiqu conetlaritasdynamicusClaritas est nihil imp fiant sollemnes feiat lla.</p>
    </div>

    <div class="service" style="left:462px">
      <svg class="badge" width="70" height="70" viewBox="0 0 70 70"><circle cx="35" cy="35" r="33" fill="#111" stroke="#3a3a3a" stroke-width="3"/>
        <circle cx="33" cy="38" r="11" fill="#e8e2b8"/><rect x="38" y="24" width="5" height="6" fill="#e8e2b8" transform="rotate(40 40 27)"/><path d="M42 24q3-4 6-3" fill="none" stroke="#e8e2b8" stroke-width="1.5"/></svg>
      <h3 class="dim">Bomb Technicians</h3>
      <p>Claritas est eteus dynamicuinquiqu conetlaritasdynamicusClaritas est nihil imp fiant sollemnes feiat lla.</p>
    </div>
  </section>

  <section class="welcome">
    <div class="soldier-photo" role="img" aria-label="Soldier in camouflage uniform and helmet standing with arms crossed"></div>
    <div class="welcome-text">
      <h2>WELCOME TO OUR SITE</h2>
      <p>Duis autem vel eum iriure dolor in hendrerit in vulputate velit esse molestie consuat, vel illum dolore eu feugiat nulla facilisis at vero eros et accumsan et iusto odio dni ssim qui blandit praesent luptatum zzril delenit.</p>
      <p>Maselementum ursus eleifender. Aenean auctor wisi et urna. Viliquam erat volutpas matsreuisac turpilnter.</p>
      <span class="read-more">READ MORE</span>
    </div>
    <div class="news">
      <h2>NEWS &amp; EVENTS</h2>
      <div class="news-item">
        <h3>TYPI NON HABENT CLARITATEM ITAM:</h3>
        <p>Typi non habent claritatem insitam; est usis tis in iis qui facit eorum claritatem Inves.</p>
      </div>
      <div class="news-item">
        <h3>TYPI NON HABENT CLARITATEM INSM:</h3>
        <p>Typi non habent claritatem insitam; est usis tis in iis qui facit eorum claritatem Inves.</p>
      </div>
    </div>
  </section>

  <footer class="site-footer">
    <div class="col testimonials">
      <h2>Testimonials</h2>
      <p class="quote">Fusce feugiat malesuada odio. Morbi nunc dogravida at, cursus nec, luctus a, lorem. Maecnas tristique orci acd se m. Lorem ipsum dolorsit amet, consectetur adipisicing elit.</p>
      <div class="author">
        <svg width="9" height="9" viewBox="0 0 10 10"><circle cx="5" cy="3" r="2.4" fill="#fff"/><path d="M0.5 10a4.5 4 0 0 1 9 0z" fill="#fff"/></svg>
        Dana Morrow
      </div>
    </div>

    <div class="col contact">
      <h2>Contact</h2>
      <ul class="contact-list">
        <li><svg width="8" height="11" viewBox="0 0 8 11"><path d="M4 0a4 4 0 0 1 4 4c0 3-4 7-4 7S0 7 0 4a4 4 0 0 1 4-4z" fill="#ccc"/><circle cx="4" cy="4" r="1.5" fill="#262626"/></svg><span>415 Harbor Point Rd.<br>Arlington VA 22201</span></li>
        <li><svg width="11" height="8" viewBox="0 0 11 8"><rect x=".5" y=".5" width="10" height="7" fill="none" stroke="#ccc"/><path d="M.5.5l5 4 5-4" fill="none" stroke="#ccc"/></svg><span>info@ridgelinetraining.net</span></li>
        <li><svg width="10" height="10" viewBox="0 0 24 24"><path fill="#ccc" d="M6.6 10.8a15.1 15.1 0 0 0 6.6 6.6l2.2-2.2a1 1 0 0 1 1-.25 11.4 11.4 0 0 0 3.6.57 1 1 0 0 1 1 1V20a1 1 0 0 1-1 1A17 17 0 0 1 3 4a1 1 0 0 1 1-1h3.5a1 1 0 0 1 1 1c0 1.25.2 2.45.57 3.57a1 1 0 0 1-.25 1z"/></svg><span>202 555 0193</span></li>
      </ul>
    </div>

    <div class="col follow">
      <h2>Follow Us</h2>
      <p>Follow us through our social network and get connected with our updates.</p>
      <div class="social" aria-label="Social network links">
        <span></span><span></span><span></span><span></span>
      </div>
    </div>

    <div class="footer-rule"></div>
    <p class="copyright">Copyright ©2013. All Rights Reserved.</p>
  </footer>

</div>
</body>
</html>
```